Beauty Salon Design

The business card design will be for a new beauty salon opening up.

The therapist has over 11 years at a leading beauty Salon in perth.

The two colours that the salon will use is black and gold.

Industry/Entity Type

Beauty Salon

Contact Information for Business Card

Lumora Beauty

Corinne Halstead Pryce
Advanced beauty therapist
0455 817 302

Monday - Friday 9am - 2.30pm
Weekends and nights by appointment only

Waxing, Tinting, Swedish massage, hot stone massage, facials, peels, micro, LED light treatment, skin needling and retail products.

```html
<!DOCTYPE html>
<html lang="en">
<head>
<meta charset="utf-8">
<title>Lumora Beauty – Business Card</title>
<link rel="stylesheet" href="https://fonts.googleapis.com/css2?family=Didact+Gothic&display=swap">
<style>
  :root {
    --stage: #5f6b6f;
    --card-black: #0b0c0d;
    --card-charcoal: #111314;
    --gold-light: #e8e612;
    --gold-mid: #c9c40c;
    --gold-deep: #9b9608;
    --gold-dark: #7d7605;
    --gold-text: #d8d31a;
    --muted-gold: #8f8a1a;
    --service-text: #6e6912;
    --ink: #1a1a0a;
  }
  * { box-sizing: border-box; margin: 0; padding: 0; }
  html, body { width: 1200px; height: 741px; overflow: hidden; }
  body {
    background: var(--stage);
    font-family: "Didact Gothic", "Helvetica Neue", Arial, sans-serif;
    position: relative;
  }
  .card {
    position: absolute;
    left: 390px;
    width: 420px;
    height: 240px;
    overflow: hidden;
    box-shadow: 0 6px 18px rgba(0,0,0,0.35);
  }
  /* Front */
  .card-front { top: 88px; background: var(--card-black); }
  .front-phone {
    position: absolute; top: 11px; right: 14px;
    display: flex; align-items: center; gap: 8px;
    color: var(--gold-text); font-size: 14px; letter-spacing: 1.5px;
  }
  .front-phone svg { width: 10px; height: 16px; }
  .brand {
    position: absolute; left: 0; right: 0; top: 96px;
    display: flex; align-items: center; justify-content: center; gap: 14px;
  }
  .brand-dot {
    width: 30px; height: 30px; border-radius: 50%;
    background: var(--gold-mid);
  }
  .brand-name {
    color: var(--gold-text); font-size: 32px; letter-spacing: 1px; line-height: 1;
  }
  /* Back */
  .card-back { top: 413px; background: var(--card-charcoal); }
  .back-band {
    position: absolute; left: 0; top: 0; width: 100%; height: 78px;
    background: linear-gradient(180deg, var(--gold-deep) 0%, var(--gold-mid) 45%, var(--gold-light) 100%);
  }
  .hours {
    position: absolute; top: 6px; right: 8px;
    color: var(--ink); font-size: 14.5px;
  }
  .therapist-name {
    position: absolute; left: 8px; top: 57px;
    color: var(--ink); font-size: 17px;
  }
  .therapist-role {
    position: absolute; left: 8px; top: 80px;
    color: var(--muted-gold); font-size: 15px;
  }
  .services {
    position: absolute; left: 174px; top: 131px;
    list-style: none; color: var(--service-text); font-size: 11.5px; line-height: 18.5px;
  }
  .services li span + span { margin-left: 10px; }
  .appointment-band {
    position: absolute; left: 0; bottom: 0; width: 100%; height: 26px;
    background: linear-gradient(90deg, var(--gold-light) 0%, var(--gold-mid) 45%, var(--gold-dark) 100%);
    color: var(--ink); font-size: 14.5px; padding: 4px 8px;
  }
</style>
</head>
<body>

<section class="card card-front" aria-label="Business card front">
  <div class="front-phone">
    <svg viewBox="0 0 10 16" aria-hidden="true">
      <rect x="0.5" y="0.5" width="9" height="15" rx="1.5" fill="none" stroke="#d8d31a"/>
      <rect x="2" y="2.5" width="6" height="8" fill="#d8d31a"/>
      <circle cx="5" cy="13" r="1" fill="#d8d31a"/>
    </svg>
    <span>0455 817 302</span>
  </div>
  <div class="brand">
    <span class="brand-dot" aria-hidden="true"></span>
    <span class="brand-name">Lumora Beauty</span>
  </div>
</section>

<section class="card card-back" aria-label="Business card back">
  <div class="back-band"></div>
  <p class="hours">Monday - Friday 9am - 2.30pm</p>
  <h1 class="therapist-name" style="font-weight:400">Corinne Halstead Pryce</h1>
  <p class="therapist-role">Advanced beauty therapist</p>
  <ul class="services">
    <li><span>hot stone massage</span></li>
    <li><span>skin needling</span><span>swedish massage</span></li>
    <li><span>retail products</span><span>waxing</span><span>tinting</span></li>
    <li><span>facials, peels, micro LED light treatment</span></li>
  </ul>
  <p class="appointment-band">Weekends and nights by appointment only</p>
</section>

</body>
</html>
```